Lattiro.com home page upgrade. Strong existing assets.

We are looking to redesign our homepage. We need to communicate three large concepts.

1) Software-as-a-Service for connected electronic device management
2) Mesh-Networking-as-a-Service allows local devices to talk together easily
3) We have 3 pieces of hardware:
A) K7 Beetle
B) K7 Moth
C) K7 Grasshopper

We will keep the color scheme, although we would like the general feel to be lighter than our current page at http://lattiro.com

See the word doc for more details.

Closing soon! Get in last designs! 

Industry/Entity Type

Electronic

Requirements
Nice to have
• large images, modern design

```html
<!DOCTYPE html>
<html lang="en">
<head>
<meta charset="utf-8">
<title>Lattiro – Your Professional Internet-of-Things Solution</title>
<link rel="stylesheet" href="https://fonts.googleapis.com/css2?family=Questrial&display=swap">
<style>
  :root {
    --plum: #3d2428;
    --plum-deep: #2d1a1d;
    --orange: #f0852d;
    --orange-light: #f5a05a;
    --white: #ffffff;
    --ink: #2b2024;
    --grey-bg: #e4e4e4;
    --grey-text: #8f8487;
  }
  * { box-sizing: border-box; margin: 0; padding: 0; }
  html, body { width: 1200px; height: 2344px; overflow: hidden; }
  body {
    font-family: "Questrial", "Century Gothic", sans-serif;
    color: var(--ink);
    background: var(--white);
    position: relative;
  }
  .block { position: absolute; left: 0; width: 1200px; }
  a { color: inherit; text-decoration: none; }

  /* header */
  .site-header { top: 0; height: 117px; background: var(--white); }
  .brand {
    position: absolute; left: 236px; top: 26px;
    font-size: 60px; line-height: 64px; color: var(--plum);
  }
  .tagline {
    position: absolute; left: 525px; top: 55px;
    font-size: 17px; font-style: italic; color: var(--orange);
  }

  /* navigation */
  .main-nav {
    top: 117px; height: 42px; background: var(--plum);
    display: flex; justify-content: center; align-items: center; gap: 28px;
  }
  .main-nav a { color: var(--white); font-size: 17px; }

  /* hero */
  .hero {
    top: 159px; height: 408px;
    background: radial-gradient(ellipse 70% 80% at 50% 50%, #ffffff 0%, #f3f3f3 55%, #d9d9d9 100%);
  }
  .hero-title { position: absolute; left: 148px; top: 56px; font-size: 50px; color: var(--orange); font-weight: 400; }
  .hero-text { position: absolute; left: 149px; top: 120px; font-size: 22px; line-height: 28px; color: var(--ink); width: 470px; }
  .hero-text + .hero-text { top: 190px; }
  .hero-link { color: var(--orange); text-decoration: underline; }
  .hero-button {
    position: absolute; left: 150px; top: 269px; width: 208px; height: 47px;
    background: var(--plum); color: var(--white); font-size: 21px;
    display: flex; align-items: center; justify-content: center; border-radius: 2px;
  }
  .slider-dots { position: absolute; left: 150px; top: 369px; display: flex; gap: 5px; }
  .slider-dots span { width: 12px; height: 12px; border-radius: 50%; background: var(--plum); }
  .slider-dots span.is-active { background: var(--orange); }
  .hero-device {
    position: absolute; left: 625px; top: 30px; width: 425px; height: 355px;
    background: linear-gradient(160deg, #f2f2f2 0%, #cfcfcf 70%, #b5b5b5 100%);
    border-radius: 24px;
  }
  .chevron { position: absolute; top: 567px; left: 562px; }

  /* OEM */
  .oem { top: 606px; height: 750px; }
  .oem-visual {
    position: absolute; left: 278px; top: 27px; width: 647px; height: 476px;
    background: linear-gradient(180deg, #e8ebf2 0%, #c7cfdf 100%);
    border-radius: 10px;
  }
  .section-title { position: absolute; left: 0; width: 1200px; text-align: center; font-weight: 400; }
  .oem .section-title { top: 518px; font-size: 60px; color: var(--orange); }
  .section-sub { position: absolute; left: 0; width: 1200px; text-align: center; font-size: 23px; }
  .oem .section-sub { top: 604px; color: var(--ink); }
  .cta {
    position: absolute; left: 436px; width: 298px; height: 55px;
    display: flex; align-items: center; justify-content: center;
    font-size: 22px; border-radius: 3px;
  }
  .oem .cta { top: 661px; background: var(--plum); color: var(--white); }

  /* integrators */
  .integrators {
    top: 1356px; height: 444px;
    background: radial-gradient(ellipse 60% 90% at 70% 40%, var(--orange-light) 0%, var(--orange) 70%);
  }
  .integrators .section-title { top: 92px; font-size: 58px; line-height: 70px; color: var(--white); }
  .integrators .section-sub { top: 240px; color: var(--white); }
  .integrators .cta { top: 300px; background: var(--white); color: var(--orange); }

  /* enterprise */
  .enterprise { top: 1800px; height: 411px; background: var(--plum); }
  .enterprise .section-title { top: 66px; font-size: 58px; line-height: 69px; color: var(--white); }
  .enterprise .section-sub { top: 225px; color: var(--white); }
  .enterprise .cta { top: 283px; background: var(--orange); color: var(--white); }

  /* footer */
  .footer-nav {
    top: 2211px; height: 34px; background: var(--plum-deep);
    display: flex; justify-content: center; align-items: center; gap: 22px;
  }
  .footer-nav a { color: var(--grey-text); font-size: 13px; }
  .site-footer { top: 2245px; height: 99px; background: var(--grey-bg); }
  .footer-brand { position: absolute; left: 154px; top: 20px; font-size: 50px; line-height: 56px; color: var(--plum); }
  .copyright { position: absolute; left: 490px; top: 51px; font-size: 11px; color: var(--ink); }
  .social { position: absolute; left: 916px; top: 30px; display: flex; gap: 10px; }
  .social a { width: 39px; height: 39px; background: #3b6fb6; display: block; }
  .social a.is-sky { background: #55a4dd; }
  .social a.is-blue { background: #1c7bb8; }
  .to-top {
    position: absolute; left: 1098px; top: 24px; width: 63px; height: 59px;
    background: var(--plum); border-radius: 3px;
    display: flex; align-items: center; justify-content: center;
  }
</style>
</head>
<body>
  <header class="block site-header">
    <div class="brand">Lattiro</div>
    <p class="tagline">Your Professional “Internet-of-Things” Solution – Today</p>
  </header>

  <nav class="block main-nav">
    <a href="#">Manufacturers</a>
    <a href="#">Technology Integrators</a>
    <a href="#">Enterprise Plans</a>
    <a href="#">K7 Devices</a>
    <a href="#">About Us</a>
    <a href="#">Contact Us</a>
  </nav>

  <section class="block hero">
    <h1 class="hero-title">Hardware</h1>
    <p class="hero-text">The K7 Beetle from Lattiro connects your devices to the Internet-to-Things</p>
    <p class="hero-text">Have your own hardware? No problem!<br><a class="hero-link" href="#">Click Here</a></p>
    <a class="hero-button" href="#">Learn More</a>
    <div class="slider-dots"><span></span><span class="is-active"></span><span></span><span></span><span></span></div>
    <div class="hero-device" role="img" aria-label="White K7 Beetle hardware module with green terminal block and network port"></div>
  </section>

  <svg class="chevron" width="76" height="40" viewBox="0 0 76 40" aria-hidden="true">
    <polygon points="0,0 76,0 38,38" fill="#d9d9d9"/>
    <polygon points="10,0 66,0 38,28" fill="#ffffff"/>
  </svg>

  <section class="block oem">
    <div class="oem-visual" role="img" aria-label="Phone and desktop monitor showing the Lattiro web and mobile app"></div>
    <h2 class="section-title">Lattiro For OEM’s</h2>
    <p class="section-sub">New Revenue! Add a Web and Mobile M2M Product-Line with Lattiro</p>
    <a class="cta" href="#">LEARN MORE</a>
  </section>

  <section class="block integrators" role="region" aria-label="Orange background with circuit pattern">
    <h2 class="section-title">Lattiro For<br>Technology Integrators</h2>
    <p class="section-sub">Enhance Your Service Offering with Connected Devices!</p>
    <a class="cta" href="#">LEARN MORE</a>
  </section>

  <section class="block enterprise">
    <h2 class="section-title">Lattiro Enterprise<br>Plans For Companies</h2>
    <p class="section-sub">Quickly get a solution running that ties to your back office</p>
    <a class="cta" href="#">LEARN MORE</a>
  </section>

  <nav class="block footer-nav">
    <a href="#">Manufacturers</a>
    <a href="#">Technology Integrators</a>
    <a href="#">Enterprise Plans</a>
    <a href="#">K7 Devices</a>
    <a href="#">About Us</a>
    <a href="#">Contact Us</a>
  </nav>

  <footer class="block site-footer">
    <div class="footer-brand">Lattiro</div>
    <p class="copyright">Copyright © 2014 lattiro. all rights reserved</p>
    <div class="social">
      <a href="#" aria-label="Social profile"></a>
      <a href="#" class="is-sky" aria-label="Social profile"></a>
      <a href="#" class="is-blue" aria-label="Social profile"></a>
    </div>
    <a class="to-top" href="#" aria-label="Back to top">
      <svg width="30" height="36" viewBox="0 0 30 36" aria-hidden="true">
        <polygon points="15,0 30,16 21,16 21,36 9,36 9,16 0,16" fill="#f0852d"/>
      </svg>
    </a>
  </footer>
</body>
</html>
```